RW Personal Name/Business Card.

I need a double-sided name card with a logo/full design incorporating the "themes/concepts" of:
Neurology, wellness, Animals, Healing, Chiropractic, lifestyle, energy, creatvity & color on both sides of the card.
Information to include:
Name: Rosalind Webb
Mobile #: 0472 816 293
Email spinerwb@mailbrook.net

Possible use of "RW Health & Chiropractic"

Target Market(s)

People of all ages looking to improve their health & lifestyle.

Industry/Entity Type

Business

```html
<!DOCTYPE html>
<html lang="en">
<head>
<meta charset="utf-8">
<title>RW Health &amp; Chiropractic – Business Card</title>
<link rel="stylesheet" href="https://fonts.googleapis.com/css2?family=Open+Sans:wght@400;700&family=Poiret+One&display=swap">
<style>
  :root {
    --page-bg: #ecebe8;
    --card-back: #4e5663;
    --card-front: #f6f6f6;
    --card-front-edge: #e7e8e9;
    --text-light: #d9dce1;
    --text-name: #5a5d62;
    --text-detail: #4f5358;
    --accent: #e8952c;
    --shadow: rgba(30, 35, 45, 0.22);
  }
  * { box-sizing: border-box; margin: 0; padding: 0; }
  html, body {
    width: 1200px;
    height: 675px;
    overflow: hidden;
    background: var(--page-bg);
  }
  .sheet {
    width: 1200px;
    height: 675px;
    display: flex;
    align-items: center;
    justify-content: center;
    gap: 60px;
  }
  .card {
    width: 520px;
    height: 297px;
    border-radius: 3px;
    box-shadow: 0 10px 28px var(--shadow);
    position: relative;
  }
  .card--back {
    background: var(--card-back);
    padding: 44px 36px;
  }
  .themes {
    font-family: "Poiret One", "Trebuchet MS", sans-serif;
    color: var(--text-light);
    font-size: 17px;
    line-height: 1.45;
    letter-spacing: 0.2px;
  }
  .card--front {
    background: linear-gradient(160deg, #ffffff 0%, var(--card-front) 45%, var(--card-front-edge) 100%);
  }
  .contact {
    position: absolute;
    left: 262px;
    top: 118px;
    font-family: "Open Sans", Arial, sans-serif;
  }
  .contact__name {
    font-size: 21px;
    font-weight: 700;
    color: var(--text-name);
    line-height: 1.1;
  }
  .contact__business {
    font-size: 14px;
    color: var(--accent);
    margin-top: 2px;
    margin-bottom: 8px;
  }
  .contact__line {
    display: flex;
    align-items: center;
    gap: 8px;
    font-size: 13.5px;
    color: var(--text-detail);
    line-height: 1.5;
  }
  .contact__icon {
    width: 11px;
    height: 11px;
    flex: none;
  }
</style>
</head>
<body>
  <main class="sheet">
    <section class="card card--back" aria-label="Card back">
      <p class="themes">
        Neurology | Wellness | Animals | Healing | Chiropractic |<br>
        Lifestyle | Energy | Creativity &amp; color on both sides.
      </p>
    </section>

    <section class="card card--front" aria-label="Card front">
      <div class="contact">
        <h1 class="contact__name">Rosalind Webb</h1>
        <p class="contact__business">RW Health &amp; Chiropractic</p>
        <p class="contact__line">
          <svg class="contact__icon" viewBox="0 0 11 11" aria-hidden="true">
            <rect x="2.5" y="0.5" width="6" height="10" rx="1.2" fill="none" stroke="var(--accent)" stroke-width="1.2"/>
            <rect x="4.5" y="8.3" width="2" height="1" fill="var(--accent)"/>
          </svg>
          0472 816 293
        </p>
        <p class="contact__line">
          <svg class="contact__icon" viewBox="0 0 11 11" aria-hidden="true">
            <rect x="0" y="1.5" width="11" height="8" rx="1" fill="var(--accent)"/>
            <path d="M0.8 2.3 L5.5 6 L10.2 2.3" fill="none" stroke="#fff" stroke-width="1"/>
          </svg>
          spinerwb@mailbrook.net
        </p>
      </div>
    </section>
  </main>
</body>
</html>
```